Crisp and clean business card for health business

I have a business that is located inside another business. I need a double sided card to communicate the two separate business names but would also like some space available to write an appointment time on the card. The background needs to be WHITE. My clients are aged from 20- 100. I would like the card to not be fussy. The address and phone number need to be very clear

Target Market(s)

Health conscious people

Industry/Entity Type

Health Care

Contact Information for Business Card

Address: Shop 17C Bellfield Shopping Centre, Elmvale 2140
Phone: 92 9431 6058
Email: stepwellpodiatry@examplemail.com

Colors
acd037
33b8a4
33a6d7

Requirements
Must have
• Must have space on one side to allow for an appointment
• To include the attached logos - one on each side

```html
<!DOCTYPE html>
<html lang="en">
<head>
<meta charset="utf-8">
<title>Stepwell Podiatry – Business Card</title>
<link rel="stylesheet" href="https://fonts.googleapis.com/css2?family=Open+Sans:wght@400;600;700&display=swap">
<style>
  :root {
    --backdrop: #26282b;
    --card: #ffffff;
    --card-shade: #f1f2f2;
    --ink: #2b2b2b;
    --rule: #3a3a3a;
    --green: #acd037;
    --teal: #33b8a4;
    --blue: #33a6d7;
    --navy: #2f6fb4;
  }
  * { margin: 0; padding: 0; box-sizing: border-box; }
  html, body {
    width: 1200px; height: 904px; overflow: hidden;
    background: var(--backdrop);
    font-family: "Open Sans", Arial, sans-serif;
    color: var(--ink);
  }
  .stage { position: relative; width: 1200px; height: 904px; }
  .card {
    position: absolute;
    width: 620px; height: 360px;
    background: linear-gradient(160deg, var(--card) 0%, var(--card) 55%, var(--card-shade) 100%);
    box-shadow: 0 18px 40px rgba(0,0,0,.55);
    overflow: hidden;
  }
  .card__band { position: absolute; left: 0; right: 0; bottom: 0; height: 12px; }

  /* Appointment side */
  .card--appointment { left: 110px; top: 64px; }
  .card--appointment .card__band { background: var(--green); }
  .host-mark {
    position: absolute; left: 0; right: 0; top: 62px;
    display: flex; align-items: center; justify-content: center; gap: 14px;
  }
  .host-mark__dot { width: 26px; height: 26px; border-radius: 50%; background: var(--green); flex: none; }
  .host-mark__name { font-size: 24px; font-weight: 700; color: #5a5a5a; letter-spacing: .5px; white-space: nowrap; }
  .appointment {
    position: absolute; left: 48px; right: 40px; top: 218px;
    font-size: 16px;
  }
  .appointment__row { display: flex; align-items: flex-end; gap: 8px; margin-bottom: 32px; }
  .appointment__label { white-space: nowrap; }
  .appointment__line { flex: 1; border-bottom: 1.5px solid var(--rule); height: 18px; }
  .appointment__unit { font-size: 14px; white-space: nowrap; }

  /* Contact side */
  .card--contact { left: 470px; top: 480px; }
  .card--contact .card__band { background: var(--navy); }
  .practice-mark {
    position: absolute; left: 0; right: 0; top: 76px;
    display: flex; align-items: center; justify-content: center; gap: 14px;
  }
  .practice-mark__dot { width: 28px; height: 28px; border-radius: 50%; background: var(--teal); flex: none; }
  .practice-mark__name { font-size: 30px; font-weight: 700; color: var(--navy); letter-spacing: .5px; white-space: nowrap; }
  .contact {
    position: absolute; left: 24px; right: 24px; bottom: 46px;
    font-size: 20px; line-height: 1.5;
    display: flex; flex-direction: column; align-items: center;
  }
  .contact__row { display: flex; align-items: center; gap: 8px; white-space: nowrap; }
  .contact__icon { width: 18px; height: 18px; flex: none; }
  .contact__sep { margin: 0 4px; color: #555; }
</style>
</head>
<body>
<main class="stage">

  <section class="card card--appointment" aria-label="Appointment side">
    <div class="host-mark">
      <span class="host-mark__dot"></span>
      <span class="host-mark__name">Ridgeway Health Professionals</span>
    </div>
    <div class="appointment">
      <div class="appointment__row">
        <span class="appointment__label">Appointment Day</span>
        <span class="appointment__line"></span>
      </div>
      <div class="appointment__row">
        <span class="appointment__label">Appointment Time</span>
        <span class="appointment__line"></span>
        <span class="appointment__unit">A.M.</span>
        <span class="appointment__line"></span>
        <span class="appointment__unit">P.M.</span>
      </div>
    </div>
    <div class="card__band"></div>
  </section>

  <section class="card card--contact" aria-label="Contact side">
    <div class="practice-mark">
      <span class="practice-mark__dot"></span>
      <span class="practice-mark__name">Stepwell Podiatry</span>
    </div>
    <div class="contact">
      <div class="contact__row">
        <svg class="contact__icon" viewBox="0 0 24 24" aria-hidden="true">
          <path fill="#2f6fb4" d="M6.6 10.8a15.1 15.1 0 0 0 6.6 6.6l2.2-2.2a1 1 0 0 1 1-.25 11.4 11.4 0 0 0 3.6.57 1 1 0 0 1 1 1V20a1 1 0 0 1-1 1A17 17 0 0 1 3 4a1 1 0 0 1 1-1h3.5a1 1 0 0 1 1 1c0 1.25.2 2.45.57 3.6a1 1 0 0 1-.25 1z"/>
        </svg>
        <span>92 9431 6058</span>
        <span class="contact__sep">|</span>
        <svg class="contact__icon" viewBox="0 0 24 24" aria-hidden="true">
          <rect x="2" y="5" width="20" height="14" rx="2" fill="#2f6fb4"/>
          <path d="M3 6.5l9 6.5 9-6.5" fill="none" stroke="#fff" stroke-width="1.8"/>
        </svg>
        <span>stepwellpodiatry@examplemail.com</span>
      </div>
      <div class="contact__row">Shop 17C Bellfield Shopping Centre, Elmvale 2140</div>
    </div>
    <div class="card__band"></div>
  </section>

</main>
</body>
</html>
```